We need a large 10' x 2 1/2' banner to hang from our 10x10 red canopy. It will be used for events to let people know who we are and to promote our business. Our business is called Silver Lantern Melody Tutoring. We offer private music lessons in students' homes and our target market is moms of kids ages 5-15. The canopy we are using is red and the colors we use for our business are red white and black. Other colors may be used, as long as the red, black and white are prominent.
I would like the background to be mostly white since it will contrast the red canopy and red table cloth.
I would like my logo to be somewhere on the banner. The problem is that I only have a low quality image of my logo. I will attach the logo, but if there is any way you can adjust the logo so it doesn't look blurred or pixelated, it would be greatly appreciated.
The part I would like to be most visible is "Music Lessons in Your Home". That will help people know right away what service we offer.
I would also like to include the instruments we teach. They are: piano, voice, guitar, woodwinds, brass, percussion. I picture these words across the bottom of the banner in horizontal orientation with round dots separating the instruments, but not necessarily. They can be placed in whatever way is most visually appealing.
Lastly, if there is room, I'd like to include the words, "We make it easy to provide an outstanding music education for your kids." If it looks too cluttered, it can be left out.
The specifications have also been attached as an image.
Moms of kids ages 5-15
Business

```html
<!DOCTYPE html>
<html lang="en">
<head>
<meta charset="utf-8">
<title>Silver Lantern Melody Tutoring – Event Banner</title>
<link rel="stylesheet" href="https://fonts.googleapis.com/css2?family=EB+Garamond:ital,wght@0,400;0,500;1,700&family=Open+Sans:wght@400;700&display=swap">
<style>
  :root {
    --red: #e2262b;
    --red-deep: #c5161c;
    --black: #141414;
    --paper: #f7f6f4;
    --paper-edge: #e9e6e1;
    --frame: #8a7448;
    --white: #ffffff;
    --gold: #c9a24a;
    --gold-light: #f0d27a;
    --gold-dark: #8d6a25;
    --wood: #9a5426;
    --wood-dark: #4a2410;
    --piano: #0a0a0a;
  }
  * { margin: 0; padding: 0; box-sizing: border-box; }
  html, body { width: 1200px; height: 1000px; overflow: hidden; background: var(--white); }
  .canvas { position: relative; width: 1200px; height: 1000px; }

  .banner {
    position: absolute; left: 16px; width: 1168px; height: 294px;
    border: 3px solid var(--frame);
    background: radial-gradient(ellipse at center, var(--white) 0%, var(--paper) 60%, var(--paper-edge) 100%);
    overflow: hidden;
  }
  .banner--clefs { top: 32px; }
  .banner--instruments { top: 370px; }

  /* large clef decoration areas */
  .clef-art {
    position: absolute; top: 12px; width: 100px; height: 268px;
    border-radius: 50px 50px 44px 44px;
    background: linear-gradient(180deg, var(--red) 0%, var(--red-deep) 100%);
  }
  .clef-art--left { left: 18px; }
  .clef-art--right { right: 18px; }

  .side-curves { position: absolute; inset: 0; width: 100%; height: 100%; }
  .side-curves path { fill: var(--red); }

  /* instrument photo areas */
  .photo { position: absolute; }
  .photo--sax {
    left: 24px; top: 28px; width: 128px; height: 130px; border-radius: 30px 60px 50px 40px;
    background: radial-gradient(ellipse at 60% 55%, var(--gold-light) 0%, var(--gold) 45%, var(--gold-dark) 100%);
  }
  .photo--guitar {
    left: 6px; top: 92px; width: 122px; height: 182px; border-radius: 40px 40px 60px 60px;
    background: radial-gradient(ellipse at 55% 72%, #c98a4e 0%, var(--wood) 45%, var(--wood-dark) 100%);
  }
  .photo--congas {
    right: 46px; top: 14px; width: 102px; height: 66px; border-radius: 14px 14px 22px 22px;
    background: linear-gradient(90deg, #7c3a14, #c06b30 20%, #7c3a14 34%, #c06b30 52%, #7c3a14 68%, #c06b30 84%, #7c3a14);
  }
  .photo--piano {
    right: 18px; top: 100px; width: 116px; height: 90px; border-radius: 40px 12px 10px 10px;
    background: linear-gradient(180deg, #3a3a3a 0%, var(--piano) 60%, #000 100%);
  }
  .photo--trumpet {
    right: 28px; top: 200px; width: 92px; height: 76px; border-radius: 20px 46px 20px 20px;
    background: radial-gradient(ellipse at 70% 30%, var(--gold-light) 0%, var(--gold) 50%, var(--gold-dark) 100%);
  }

  .brand-name {
    position: absolute; left: 0; width: 100%; text-align: center;
    font-family: "EB Garamond", Georgia, serif; font-weight: 400; color: var(--red);
  }
  .banner .brand-name { top: 22px; font-size: 54px; line-height: 60px; }

  .headline {
    position: absolute; left: 0; width: 100%; text-align: center;
    font-family: "Open Sans", Arial, sans-serif; color: var(--red); text-transform: uppercase;
  }
  .headline span { display: inline-block; border-bottom: 2px solid var(--red); padding: 0 4px 1px; }
  .banner--clefs .headline { top: 170px; font-size: 35px; line-height: 44px; }
  .banner--instruments .headline { top: 164px; font-size: 30px; line-height: 48px; }
  .headline strong { font-size: 45px; font-weight: 700; }

  .tagline {
    position: absolute; left: 0; width: 100%; text-align: center;
    font-family: "Open Sans", Arial, sans-serif; font-size: 19.5px; letter-spacing: 0.3px;
    color: var(--black); text-transform: uppercase;
  }
  .banner--clefs .tagline { top: 222px; }
  .banner--instruments .tagline { top: 214px; }

  .instrument-list {
    position: absolute; left: 0; width: 100%; text-align: center;
    font-family: "EB Garamond", Georgia, serif; font-style: italic; font-weight: 700;
    font-size: 26px; letter-spacing: 2.4px; color: var(--red); text-transform: uppercase;
    text-decoration: underline; text-decoration-thickness: 1.5px; text-underline-offset: 4px;
  }
  .banner--clefs .instrument-list { top: 248px; }
  .banner--instruments .instrument-list { top: 244px; }

  .logo-standalone { position: absolute; left: 150px; top: 710px; width: 900px; height: 230px; }
  .logo-standalone .brand-name { top: 8px; font-size: 96px; line-height: 104px; }
</style>
</head>
<body>
<main class="canvas">

  <section class="banner banner--clefs" aria-label="Banner version with red clefs">
    <div class="clef-art clef-art--left" role="img" aria-label="Large red treble clef decoration"></div>
    <div class="clef-art clef-art--right" role="img" aria-label="Large red treble clef decoration"></div>
    <h1 class="brand-name">Silver Lantern<br>Melody Tutoring</h1>
    <p class="headline"><span>Music Lessons in Your Home</span></p>
    <p class="tagline">We make it easy to provide an outstanding music education for your kids</p>
    <p class="instrument-list">Piano .Voice . Guitar .Woodwinds . Brass . Percussion</p>
  </section>

  <section class="banner banner--instruments" aria-label="Banner version with instruments">
    <svg class="side-curves" viewBox="0 0 1168 294" preserveAspectRatio="none" aria-hidden="true">
      <path d="M0 0 H135 Q40 150 118 294 H0 Z"/>
      <path d="M1168 0 H1045 Q1140 150 1055 294 H1168 Z"/>
    </svg>
    <div class="photo photo--guitar" role="img" aria-label="Photo of an acoustic guitar"></div>
    <div class="photo photo--sax" role="img" aria-label="Photo of a saxophone"></div>
    <div class="photo photo--congas" role="img" aria-label="Photo of conga drums"></div>
    <div class="photo photo--piano" role="img" aria-label="Photo of a grand piano"></div>
    <div class="photo photo--trumpet" role="img" aria-label="Photo of a trumpet"></div>
    <h2 class="brand-name">Silver Lantern<br>Melody Tutoring</h2>
    <p class="headline"><strong>Music</strong> Lessons in Your Home</p>
    <p class="tagline">We make it easy to provide an outstanding music education for your kids</p>
    <p class="instrument-list">Piano .Voice . Guitar .Woodwinds . Brass . Percussion</p>
  </section>

  <section class="logo-standalone" aria-label="Brand name">
    <h2 class="brand-name">Silver Lantern<br>Melody Tutoring</h2>
  </section>

</main>
</body>
</html>
```